Operator Qualification Testing Flyer

I have a 8x10 basic flyer that I created usin InDesign for one of our services our company provides. I would like to see more options for the layout and general design of the flyer. This flyer will be used as a template for the other services we provide. I will include the InDesign Folder with all the logos and images. Please feel free to use any logo design within the folder and you can change the font and/or colors as needed. I would like the final output in a Indesign package folder to be used in InDesign 2021

Target Market(s)

Business to Business marketing in the Oil and Gas industry

Font styles to use
Sans Serif

Colors
85cae6
85acd3
3377b5
0355a3
0792cd
ffffff
cedeed

Requirements
Must have
• I included/attached a couple of brochures styles that I do like.

```html
<!DOCTYPE html>
<html lang="en">
<head>
<meta charset="utf-8">
<title>Pipeline OQ Testing Flyer</title>
<link href="https://fonts.googleapis.com/css2?family=Poppins:wght@400;500;600;700;800&display=swap" rel="stylesheet">
<style>
  :root{
    --page-bg:#d6d7d9;
    --paper:#ffffff;
    --teal-dark:#146a86;
    --teal-mid:#1b7f9f;
    --blue-bright:#2f9fcb;
    --blue-light:#38a5d2;
    --heading-grey:#54585c;
    --body-grey:#5f6368;
    --bar-grey:#e8eaeb;
    --ink:#1f2326;
    --white:#ffffff;
  }
  *{margin:0;padding:0;box-sizing:border-box;}
  html,body{width:1200px;height:927px;overflow:hidden;background:var(--page-bg);}
  body{position:relative;font-family:"Poppins",sans-serif;}
  .flyer{
    position:absolute;left:248px;top:23px;width:970px;height:1211px;
    transform:scale(0.7267);transform-origin:top left;
    background:var(--paper);overflow:hidden;
  }
  .flyer-shapes{position:absolute;inset:0;}
  .brand-name{
    position:absolute;left:40px;top:84px;
    font-weight:700;font-size:34px;line-height:1.1;color:var(--ink);
    display:flex;align-items:center;gap:16px;
  }
  .brand-dot{width:26px;height:26px;border-radius:50%;background:var(--blue-bright);flex:none;}
  .title{
    position:absolute;left:38px;top:262px;
    font-weight:800;font-size:60px;line-height:0.95;color:var(--white);letter-spacing:-0.5px;
  }
  .title-rule{position:absolute;left:38px;top:400px;width:62px;height:6px;background:var(--white);}
  .section-heading{
    position:absolute;left:75px;font-weight:700;font-size:20.4px;line-height:1.2;color:var(--heading-grey);
  }
  .body-copy{
    position:absolute;left:35px;width:445px;font-size:17.2px;line-height:26.4px;color:var(--body-grey);
  }
  .body-copy strong{font-weight:600;color:var(--heading-grey);}
  .provide-heading{
    position:absolute;left:604px;top:514px;font-weight:700;font-size:20.4px;line-height:1.2;color:var(--white);
  }
  .provide-copy{
    position:absolute;left:564px;top:562px;width:372px;font-size:17px;line-height:26.4px;color:var(--white);
  }
  .provide-copy p + p{margin-top:14px;}
  .contact-phone{
    position:absolute;left:102px;top:1094px;font-weight:700;font-size:47px;line-height:1.2;color:var(--white);letter-spacing:1px;
  }
  .contact-email{
    position:absolute;left:102px;top:1154px;font-size:24px;line-height:1.3;color:var(--white);
  }
  .contact-email b{font-weight:700;}
</style>
</head>
<body>
<main class="flyer">
  <svg class="flyer-shapes" width="970" height="1211" viewBox="0 0 970 1211">
    <defs>
      <linearGradient id="bandGradient" x1="0" y1="0" x2="1" y2="1">
        <stop offset="0" stop-color="#2f9fcb"/>
        <stop offset="1" stop-color="#17708e"/>
      </linearGradient>
      <linearGradient id="photoGradient" x1="0" y1="0" x2="0" y2="1">
        <stop offset="0" stop-color="#c9ccce"/>
        <stop offset="0.55" stop-color="#d9a24a"/>
        <stop offset="1" stop-color="#9a7a56"/>
      </linearGradient>
      <linearGradient id="panelGradient" x1="0" y1="0" x2="0" y2="1">
        <stop offset="0" stop-color="#146a86"/>
        <stop offset="1" stop-color="#1b7f9f"/>
      </linearGradient>
    </defs>

    <polygon role="img" aria-label="Photo: yellow pipelayer machines lowering a steel pipe on a construction site"
      points="345,0 970,0 970,460 330,460 520,230" fill="url(#photoGradient)"/>

    <polygon points="0,232 492,232 330,460 0,460" fill="url(#bandGradient)"/>
    <polyline points="335,0 528,230 330,462" fill="none" stroke="#146a86" stroke-width="9"/>

    <polygon points="523,460 970,460 970,1045 560,1045 523,1008" fill="url(#panelGradient)"/>
    <polygon points="540,1148 970,1148 970,1211 496,1211" fill="var(--blue-light)"/>

    <polygon points="0,498 500,498 468,546 0,546" fill="var(--bar-grey)"/>
    <polygon points="35,510 57,522 35,534" fill="var(--blue-bright)"/>
    <polygon points="0,878 500,878 468,926 0,926" fill="var(--bar-grey)"/>
    <polygon points="35,890 57,902 35,914" fill="var(--blue-bright)"/>

    <polygon points="565,517 587,529 565,541" fill="var(--white)"/>

    <polygon points="0,1086 495,1086 540,1148 495,1211 0,1211" fill="url(#bandGradient)"/>
    <circle cx="57" cy="1126" r="20" fill="none" stroke="#ffffff" stroke-width="4"/>
    <path d="M49 1116 q-3 4 1 11 q5 9 13 11 l4 -5 l-6 -4 l-3 3 q-4 -2 -6 -7 l3 -3 l-3 -6 z" fill="#ffffff"/>
    <rect x="43" y="1162" width="30" height="20" fill="#ffffff"/>
    <polyline points="43,1162 58,1174 73,1162" fill="none" stroke="#1b7f9f" stroke-width="2.5"/>

    <circle cx="748" cy="1065" r="120" fill="#ffffff"/>
    <circle role="img" aria-label="Illustration: round yellow petroleum pipeline warning marker"
      cx="748" cy="1065" r="110" fill="#f2ac1c" stroke="#1f1f1f" stroke-width="8"/>
  </svg>

  <div class="brand-name"><span class="brand-dot"></span><span>Meridian Field<br>Services</span></div>

  <h1 class="title">PIPELINE OQ<br>TESTING</h1>
  <div class="title-rule"></div>

  <h2 class="section-heading" style="top:508px;">WHAT IS OPERATOR QUALIFICATION?</h2>
  <p class="body-copy" style="top:562px;"><strong>Operator Qualifications (OQ) for DOT Oil/Gas Pipelines are requirements set by Department of Transportation (DOT) and Pipeline and Hazardous Materials Safety Administration (PHMSA).</strong> To assure safety in the transport of hazardous gases and liquids in the nation’s pipelines, pipeline operators who perform covered tasks must be qualified. Qualified means that an individual has been evaluated and can perform assigned covered tasks and recognize and react to abnormal operating conditions.</p>

  <h2 class="section-heading" style="top:888px;">WHAT ARE COVERED TASKS?</h2>
  <p class="body-copy" style="top:942px;">Covered tasks are defined in an operator’s written plan which defines specific job functions or activities personnel are qualified to perform on a pipeline facility.</p>

  <h2 class="provide-heading">WHAT WE PROVIDE</h2>
  <div class="provide-copy">
    <p>Meridian Field Services utilizes TrainCore pipeline program to administer OQ assessment testing on 127 covered tasks Upon completion of OQ testing the information is first transferred to TrainCore’s Registry System and automatically uploaded to SafeLedger.</p>
    <p>In addition to the benefits provided by SafeLedger’s database, the TrainCore Registry System houses all the completion information allowing candidates to share their training information and employers to verify successful covered task and level completions.</p>
  </div>

  <div class="contact-phone">555-014-2283</div>
  <div class="contact-email">alex@<b>meridianfield</b>.co</div>
</main>
</body>
</html>
```